Building/Renovation Company needs Website

I need a website designed for a renovation/building company based in Hampshire. We specialise in kitchens, bathrooms, carpentry, plastering, brickwork, ground/garden works and decorating, and all our work is fully insured and carried out to a high standard.

With the photos, display them in a before/after format.

Coded - Design and coding required

1 page

```html
<!DOCTYPE html>
<html lang="en">
<head>
<meta charset="utf-8">
<title>Harwell Builds – Property Renovation &amp; Building Services</title>
<link href="https://fonts.googleapis.com/css2?family=Montserrat:wght@500;600;700;800&family=Poppins:wght@400;500;600&family=Oswald:wght@600&display=swap" rel="stylesheet">
<style>
:root{
  --blue:#2a3192;
  --yellow:#d4dc1f;
  --ink:#1d1d1f;
  --grey:#4a4a4a;
  --white:#ffffff;
}
*{margin:0;padding:0;box-sizing:border-box}
html,body{width:1200px;height:3982px;overflow:hidden;background:var(--white)}
body{position:relative;font-family:'Poppins',sans-serif;color:var(--ink)}
.abs{position:absolute}
.fill{position:absolute}
/* header */
.topbar{left:688px;top:0;width:512px;height:51px;background:var(--blue);clip-path:polygon(0 0,100% 0,100% 100%,30px 100%);color:var(--white);font-size:14px;font-weight:500;display:flex;align-items:center;gap:26px;padding-left:66px}
.topbar span{display:flex;align-items:center;gap:8px}
.brand{font-family:'Poppins',sans-serif;font-weight:500;color:var(--blue);display:flex;align-items:center;gap:10px}
.brand i{display:block;width:22px;height:22px;background:var(--yellow)}
.header-brand{left:74px;top:44px;font-size:26px}
.nav{top:76px;left:0;width:1200px;font-family:'Montserrat',sans-serif;font-weight:600;font-size:15px;color:var(--ink)}
.nav a{position:absolute;text-decoration:none;color:inherit}
.nav a.active{color:var(--blue)}
.nav a.active::after{content:"";position:absolute;left:0;right:0;top:28px;height:3px;background:var(--yellow)}
.hero{left:0;top:121px;width:1200px;height:541px;background:linear-gradient(100deg,#6f6a64 0%,#9b8f81 35%,#7a6a5a 65%,#5d4c3e 100%)}
.hero::after{content:"";position:absolute;inset:0;background:linear-gradient(180deg,rgba(0,0,0,.15),rgba(40,30,20,.35))}
.hero h1{position:absolute;left:0;width:1200px;top:160px;text-align:center;font-family:'Oswald',sans-serif;font-weight:600;font-size:72px;line-height:78px;color:var(--white);z-index:1;letter-spacing:.5px}
/* intro */
.intro-title{left:127px;top:786px;width:430px;font-family:'Montserrat',sans-serif;font-weight:700;font-size:30px;line-height:35px;color:var(--blue)}
.body-copy{font-size:15px;line-height:24px;color:var(--grey)}
.intro-copy{left:127px;top:942px;width:430px}
.btn{display:flex;align-items:center;justify-content:center;background:var(--yellow);color:var(--blue);font-family:'Montserrat',sans-serif;font-weight:700;font-size:16px;width:150px;height:50px}
.section-title{left:0;width:1200px;text-align:center;font-family:'Montserrat',sans-serif;font-weight:800;font-size:45px;color:var(--blue)}
/* services */
.card{top:1449px;width:244px;height:341px;background:var(--white);box-shadow:0 4px 18px rgba(0,0,0,.09);border-radius:6px;overflow:hidden}
.card .photo{height:164px}
.card h3{font-family:'Montserrat',sans-serif;font-weight:600;font-size:20px;margin:36px 0 6px 21px}
.card p{font-size:14px;line-height:18px;color:var(--grey);margin:0 21px}
/* about */
.about-band{left:0;top:2370px;width:1200px;height:509px;background:var(--blue)}
.about-photo{left:0;top:1929px;width:601px;height:528px;border-radius:0 26px 26px 0;background:linear-gradient(120deg,#2c3345 0%,#3c4559 40%,#c9ccd0 60%,#a78c6e 100%)}
.about-title{left:649px;top:1966px;font-family:'Montserrat',sans-serif;font-weight:800;font-size:45px;color:var(--blue)}
.about-copy{left:649px;top:2036px;width:440px}
.why-title{top:2548px;color:var(--white)}
.why{top:2680px;width:220px;text-align:center;color:var(--white);font-family:'Montserrat',sans-serif;font-weight:600;font-size:19px;line-height:22px}
.why svg{display:block;margin:0 auto 14px;height:52px}
.stripe{left:0;top:2879px;width:1200px;height:23px;background:var(--yellow)}
/* projects */
.project{top:3089px;width:500px;height:283px;display:flex}
.project div{flex:1;position:relative}
.tag{position:absolute;bottom:14px;background:var(--yellow);color:var(--blue);font-family:'Montserrat',sans-serif;font-weight:700;font-size:16px;padding:8px 20px}
/* cta */
.cta{left:0;top:3493px;width:1200px;height:142px;background:var(--blue);color:var(--white)}
.cta h2{position:absolute;left:326px;top:48px;font-family:'Montserrat',sans-serif;font-weight:700;font-size:37px}
.cta a{position:absolute;left:690px;top:60px;font-family:'Montserrat',sans-serif;font-weight:700;font-size:16px;color:var(--white);text-decoration:none}
.cta .tool{position:absolute;left:880px;top:30px;width:135px;height:112px;background:linear-gradient(135deg,#8b8f96 0%,#8b8f96 40%,#a0683a 60%,#7a4d2a 100%);border-radius:6px}
/* footer */
.footer-brand{left:124px;top:3700px;font-size:28px}
.fcol{top:3700px;font-size:15px;line-height:24px;color:var(--grey)}
.fcol h4{font-family:'Montserrat',sans-serif;font-weight:700;font-size:20px;color:var(--ink);margin-bottom:12px}
.fcol .row{display:flex;align-items:flex-start;gap:10px;margin-bottom:8px}
.fcol .dot{flex:none;width:26px;height:26px;border-radius:50%;background:var(--blue);display:flex;align-items:center;justify-content:center}
.rule{left:0;top:3907px;width:1200px;height:2px;background:#222}
.copyright{left:0;top:3940px;width:1200px;text-align:center;font-size:15px;color:var(--grey)}
</style>
</head>
<body>

<header>
  <div class="abs topbar">
    <span><svg width="14" height="14" viewBox="0 0 24 24"><path fill="#d4dc1f" d="M6.6 10.8a15 15 0 0 0 6.6 6.6l2.2-2.2a1 1 0 0 1 1-.25 11.4 11.4 0 0 0 3.6.57 1 1 0 0 1 1 1V20a1 1 0 0 1-1 1A17 17 0 0 1 3 4a1 1 0 0 1 1-1h3.5a1 1 0 0 1 1 1c0 1.25.2 2.45.57 3.57a1 1 0 0 1-.25 1z"/></svg>0700 123 4567</span>
    <span><svg width="14" height="12" viewBox="0 0 24 20"><rect width="24" height="20" rx="2" fill="#d4dc1f"/><path d="M2 3l10 8 10-8" stroke="#2a3192" stroke-width="2" fill="none"/></svg>hello@harwellbuilds.co.uk</span>
  </div>
  <div class="abs brand header-brand"><i></i>HARWELL BUILDS</div>
  <nav class="abs nav">
    <a class="active" style="left:407px">HOME</a>
    <a style="left:495px">ABOUT US</a>
    <a style="left:617px">SERVICES</a>
    <a style="left:734px">WHY CHOOSE US?</a>
    <a style="left:920px">GALLERY</a>
    <a style="left:1033px">CONTACT</a>
  </nav>
</header>

<section class="abs hero" role="img" aria-label="Photo of a renovated open-plan kitchen and living room">
  <h1>PROPERTY RENOVATION<br>&amp; BUILDING SERVICES</h1>
</section>

<section>
  <h2 class="abs intro-title">Delivering High-Quality workmanship across Hamphire and surrounding counties.</h2>
  <p class="abs body-copy intro-copy">Lorem ipsum dolor sit amet, consectetur adipiscing elit, sed do eiusmod tempor incididunt ut labore et dolore magna aliqua. Quis ipsum suspendisse ultrices gravida. Risus commodo viverra maecenas accumsan lacus vel facilisis. Lorem ipsum dolor sit amet, consectetur adipi scing elit, sed do eiusmod tempor inc ididunt ut labore et dolore magna aliqua. Quis ipsumsusp endisse ult rices gravidsus commodo viverra maecenas.</p>
  <a class="abs btn" style="left:127px;top:1163px">READ MORE</a>
  <div class="fill" style="left:626px;top:801px;width:255px;height:405px;background:linear-gradient(180deg,#e8e8e6 0%,#c9c7c2 45%,#2d3447 70%,#6d5a48 100%)" role="img" aria-label="Photo of a renovated kitchen with dark cabinets"></div>
  <div class="fill" style="left:898px;top:870px;width:187px;height:292px;background:linear-gradient(180deg,#b8c7d6 0%,#b65f42 40%,#6e6259 70%,#8a7765 100%)" role="img" aria-label="Photo of a rooftop decking terrace"></div>
</section>

<section>
  <h2 class="abs section-title" style="top:1355px">OUR SERVICES</h2>
  <article class="abs card" style="left:77px"><div class="photo" role="img" aria-label="Photo of rooftop decking" style="background:linear-gradient(180deg,#c9d3dc,#b6634a 45%,#6f6457)"></div><h3>Brickwork</h3><p>Lorem ipsum dolor sitame consectetur adipiscingeli sed do eiusmod tempor incididunt ut labor.</p></article>
  <article class="abs card" style="left:342px"><div class="photo" role="img" aria-label="Photo of a cleared rear garden" style="background:linear-gradient(180deg,#e6e6e4,#9a8571 55%,#5a4b3e)"></div><h3>Carpentry</h3><p>Lorem ipsum dolor sitame consectetur adipiscingeli sed do eiusmod tempor incididunt ut labor.</p></article>
  <article class="abs card" style="left:606px"><div class="photo" role="img" aria-label="Photo of a renovated bathroom" style="background:linear-gradient(180deg,#eef0f1,#d8dcde 60%,#555)"></div><h3>Bathroom Fittings</h3><p>Lorem ipsum dolor sitame consectetur adipiscingeli sed do eiusmod tempor incididunt ut labor.</p></article>
  <article class="abs card" style="left:870px"><div class="photo" role="img" aria-label="Photo of a fitted kitchen" style="background:linear-gradient(180deg,#2b3347,#cfcfcc 50%,#2d3447)"></div><h3>Kitchen Fittings</h3><p>Lorem ipsum dolor sitame consectetur adipiscingeli sed do eiusmod tempor incididunt ut labor.</p></article>
</section>

<section>
  <div class="abs about-band"></div>
  <div class="abs about-photo" role="img" aria-label="Photo of a fitted kitchen with navy tiles and a window"></div>
  <h2 class="abs about-title">ABOUT US</h2>
  <p class="abs body-copy about-copy">Lorem ipsum dolor sit amet, consectetur adipiscing sed do eiusmod tempor incididunt ut labore et dolore magna aliqua. Quis ipsum suspendisse ultrices gravida. Risus commodo viverra maecenas accumsan lacus vel facilisis. Lorem ipsum dolor sit amet, consectetur adipiscing elit, sed do eiusmod tempor inc ididunt ut labore et dolore magna aliqua. Quis ipsumsusp endi sse ultrices gravida. Risus commodo viverra maece nas accumsan lacus vel facilisis.</p>
  <a class="abs btn" style="left:649px;top:2277px">READ MORE</a>

  <h2 class="abs section-title why-title">WHY CHOOSE US?</h2>
  <div class="abs why" style="left:63px"><svg viewBox="0 0 24 24"><path fill="#d4dc1f" d="M10 1h4l.6 3 2 .9 2.6-1.7 2.8 2.8-1.7 2.6.9 2 3 .6v4l-3 .6-.9 2 1.7 2.6-2.8 2.8-2.6-1.7-2 .9-.6 3h-4l-.6-3-2-.9-2.6 1.7-2.8-2.8 1.7-2.6-.9-2-3-.6v-4l3-.6.9-2L2.8 5.8l2.8-2.8 2.6 1.7 2-.9zM12 8a4 4 0 1 0 0 8 4 4 0 0 0 0-8z"/></svg>Fully Insured</div>
  <div class="abs why" style="left:284px;top:2672px"><svg viewBox="0 0 24 24"><circle cx="12" cy="7" r="5" fill="#d4dc1f"/><path fill="#d4dc1f" d="M2 23c0-6 4.5-9 10-9s10 3 10 9z"/></svg>Reliable,<br>Professional Team</div>
  <div class="abs why" style="left:515px;top:2672px"><svg viewBox="0 0 24 24"><path fill="#d4dc1f" d="M12 1l10 4v6c0 6.5-4.3 11-10 12C6.3 22 2 17.5 2 11V5zm0 3v16c4-1.2 7-4.6 7-9V7z"/></svg>High-Quality<br>Finishes</div>
  <div class="abs why" style="left:714px"><svg viewBox="0 0 24 24"><text x="12" y="21" text-anchor="middle" font-family="Montserrat,sans-serif" font-weight="800" font-size="24" fill="#d4dc1f">$</text></svg>Competitive</div>
  <div class="abs why" style="left:903px;top:2672px"><svg viewBox="0 0 24 24"><path fill="#d4dc1f" d="M23 1L1 11l7 3 11-9-9 11v7l4-5 5 3z"/></svg>Pricing<br>Free quotes</div>
  <div class="abs stripe"></div>
</section>

<section>
  <h2 class="abs section-title" style="top:2993px">OUR LATEST PROJECTS</h2>
  <div class="abs project" style="left:85px">
    <div role="img" aria-label="Before photo of an overgrown rear garden" style="background:linear-gradient(180deg,#d4d8dc,#b9b7b0 45%,#5f6b45)"><span class="tag" style="left:124px">BEFORE</span></div>
    <div role="img" aria-label="After photo of the cleared rear garden" style="background:linear-gradient(180deg,#e8e8e6,#b3a99d 50%,#5d4d3f)"><span class="tag" style="left:154px">AFTER</span></div>
  </div>
  <div class="abs project" style="left:615px">
    <div role="img" aria-label="Before photo of a bathroom with a shower enclosure" style="background:linear-gradient(180deg,#f0f0ef,#d9d9d7 60%,#bdbcb9)"><span class="tag" style="left:124px">BEFORE</span></div>
    <div role="img" aria-label="After photo of the renovated bathroom" style="background:linear-gradient(180deg,#f2f2f2,#d6d6d3 60%,#3a3a3a)"><span class="tag" style="left:154px">AFTER</span></div>
  </div>
</section>

<section class="abs cta">
  <h2>FREE ESTIMATE</h2>
  <a>CONTACT US</a>
  <div class="tool" role="img" aria-label="Illustration of a claw hammer"></div>
</section>

<footer>
  <div class="abs brand footer-brand"><i></i>HARWELL BUILDS</div>
  <div class="abs fcol" style="left:407px"><h4>Links</h4>Privacy Policy<br>Terms Of Use<br>Sitemap</div>
  <div class="abs fcol" style="left:601px"><h4>Menu</h4>Home<br>About Us<br>Services<br>Gallery<br>Contact</div>
  <div class="abs fcol" style="left:784px"><h4>Contact</h4>
    <div class="row"><span class="dot"><svg width="12" height="10" viewBox="0 0 24 20"><rect width="24" height="20" rx="2" fill="none" stroke="#d4dc1f" stroke-width="2.5"/><path d="M2 3l10 8 10-8" stroke="#d4dc1f" stroke-width="2.5" fill="none"/></svg></span>hello@harwellbuilds.co.uk</div>
    <div class="row"><span class="dot"><svg width="12" height="12" viewBox="0 0 24 24"><path fill="#d4dc1f" d="M6.6 10.8a15 15 0 0 0 6.6 6.6l2.2-2.2a1 1 0 0 1 1-.25 11.4 11.4 0 0 0 3.6.57 1 1 0 0 1 1 1V20a1 1 0 0 1-1 1A17 17 0 0 1 3 4a1 1 0 0 1 1-1h3.5a1 1 0 0 1 1 1c0 1.25.2 2.45.57 3.57a1 1 0 0 1-.25 1z"/></svg></span>0700 123 4567</div>
    <div class="row"><span class="dot"><svg width="12" height="14" viewBox="0 0 24 28"><path fill="#d4dc1f" d="M12 0a10 10 0 0 0-10 10c0 7 10 18 10 18s10-11 10-18A10 10 0 0 0 12 0zm0 14a4 4 0 1 1 0-8 4 4 0 0 1 0 8z"/></svg></span><span style="line-height:19px">12 Oak Lane, Unit 3<br>Winchester, SO23 0AB</span></div>
  </div>
  <div class="abs rule"></div>
  <p class="abs copyright">© 2025 Harwell Builds. All Rights Reserved.</p>
</footer>

</body>
</html>
```